medical practice needs a printed banner design

we need a printed banner for a new pain management medical practice in Las Vegas. The name of the practice is "Marlowe Pain Relief Center".
39" x 80" vertical banner
the look should be modern, clean, professional and in line with design of website. Please visit the website for more information regarding the practice.

Target Market(s)

age typically 40+, patients with back pain, joint pain

Industry/Entity Type

Doctor

Requirements
Must have
• our logo (attached file)
• phone number: (702) 555-0187
• website address: marlowepaincarecenter.example
• Hablamos EspaƱol
Nice to have
• slogan: Live Better (banner does not necessarily need to include slogan, but would be preferred)
• maybe a photo of spine, or photo depicting back pain, or active lifestyle
Should not have
• please do not include physical address location as we will be relocating
• * in addition, we hope the banner is not to be misconstrued as a chiropractic
• practice

```html
<!DOCTYPE html>
<html lang="en">
<head>
<meta charset="utf-8">
<title>Marlowe Pain Relief Center – Banner</title>
<link rel="stylesheet" href="https://fonts.googleapis.com/css2?family=Raleway:wght@400;500;600;700&display=swap">
<style>
  :root {
    --navy: #2b2b63;
    --teal: #4fb7c3;
    --teal-light: #8fd3da;
    --white: #ffffff;
    --photo-foliage-dark: #2f4a24;
    --photo-foliage: #6f9a48;
    --photo-leaf-light: #a9c77a;
    --photo-shirt: #a3303a;
    --photo-skin: #d9a27f;
    --photo-cloth: #eef3f6;
  }
  html, body {
    margin: 0;
    padding: 0;
    width: 1200px;
    height: 2400px;
    overflow: hidden;
    background: var(--white);
  }
  .banner {
    position: relative;
    width: 1200px;
    height: 2400px;
    overflow: hidden;
    font-family: "Raleway", Arial, sans-serif;
    background: var(--white);
  }
  .banner-shapes {
    position: absolute;
    inset: 0;
    width: 1200px;
    height: 2400px;
  }
  .brand {
    position: absolute;
    top: 100px;
    left: 0;
    width: 1200px;
    text-align: center;
    color: var(--navy);
    font-weight: 500;
  }
  .brand-mark {
    display: block;
    width: 64px;
    height: 64px;
    margin: 0 auto 20px;
    background: var(--navy);
  }
  .brand-name {
    display: block;
    font-size: 104px;
    letter-spacing: 4px;
    line-height: 1;
    text-transform: uppercase;
  }
  .brand-sub {
    display: block;
    margin-top: 18px;
    font-size: 40px;
    letter-spacing: 6px;
    color: var(--teal);
    text-transform: uppercase;
  }
  .slogan {
    position: absolute;
    top: 446px;
    left: 520px;
    width: 680px;
    height: 132px;
    box-sizing: border-box;
    padding: 4px 0 0 26px;
    background: var(--teal);
    color: var(--white);
  }
  .slogan-title {
    display: block;
    font-size: 88px;
    font-weight: 500;
    line-height: 1.05;
  }
  .slogan-sub {
    display: block;
    font-size: 28px;
    font-weight: 500;
    margin-left: 40px;
  }
  .contact {
    position: absolute;
    left: 70px;
    top: 1810px;
    width: 560px;
    color: var(--white);
    font-size: 60px;
    font-weight: 500;
    line-height: 72px;
  }
  .contact-rule {
    position: absolute;
    left: 70px;
    top: 2120px;
    width: 560px;
    height: 3px;
    background: var(--white);
  }
  .language {
    position: absolute;
    left: 0;
    top: 2180px;
    width: 1200px;
    text-align: center;
    color: var(--navy);
    font-size: 64px;
    font-weight: 700;
    line-height: 90px;
    letter-spacing: 1px;
  }
  .web-bar {
    position: absolute;
    left: 0;
    bottom: 0;
    width: 1200px;
    height: 110px;
    background: var(--navy);
    color: var(--white);
    font-size: 50px;
    font-weight: 500;
    line-height: 110px;
    text-align: center;
  }
</style>
</head>
<body>
<main class="banner">
  <svg class="banner-shapes" viewBox="0 0 1200 2400" xmlns="http://www.w3.org/2000/svg">
    <defs>
      <linearGradient id="foliageTones" x1="0" y1="0" x2="1" y2="1">
        <stop offset="0" stop-color="var(--photo-foliage-dark)"/>
        <stop offset="0.5" stop-color="var(--photo-foliage)"/>
        <stop offset="1" stop-color="var(--photo-foliage-dark)"/>
      </linearGradient>
      <radialGradient id="leafGlow" cx="0.75" cy="0.2" r="0.4">
        <stop offset="0" stop-color="var(--photo-leaf-light)" stop-opacity="0.8"/>
        <stop offset="1" stop-color="var(--photo-leaf-light)" stop-opacity="0"/>
      </radialGradient>
      <radialGradient id="shirtGlow" cx="0.3" cy="0.5" r="0.32">
        <stop offset="0" stop-color="var(--photo-shirt)" stop-opacity="0.85"/>
        <stop offset="1" stop-color="var(--photo-shirt)" stop-opacity="0"/>
      </radialGradient>
      <radialGradient id="skinGlow" cx="0.62" cy="0.42" r="0.3">
        <stop offset="0" stop-color="var(--photo-skin)" stop-opacity="0.85"/>
        <stop offset="1" stop-color="var(--photo-skin)" stop-opacity="0"/>
      </radialGradient>
      <radialGradient id="clothGlow" cx="0.85" cy="0.72" r="0.3">
        <stop offset="0" stop-color="var(--photo-cloth)" stop-opacity="0.85"/>
        <stop offset="1" stop-color="var(--photo-cloth)" stop-opacity="0"/>
      </radialGradient>
    </defs>
    <polygon class="corner-accent" points="650,0 1200,0 1200,340" fill="var(--navy)"/>
    <g class="photo-area" role="img" aria-label="Photo of a smiling mother and son outdoors beside a swing">
      <polygon points="330,390 1200,380 1200,2160 0,2160 0,1000" fill="url(#foliageTones)"/>
      <polygon points="330,390 1200,380 1200,2160 0,2160 0,1000" fill="url(#leafGlow)"/>
      <polygon points="330,390 1200,380 1200,2160 0,2160 0,1000" fill="url(#shirtGlow)"/>
      <polygon points="330,390 1200,380 1200,2160 0,2160 0,1000" fill="url(#skinGlow)"/>
      <polygon points="330,390 1200,380 1200,2160 0,2160 0,1000" fill="url(#clothGlow)"/>
    </g>
    <path class="curve-light" d="M0,1160 C300,1420 700,1880 1200,1980 L1200,2040 C700,1950 300,1500 0,1240 Z" fill="var(--teal-light)"/>
    <path class="curve-teal" d="M0,1230 C300,1490 700,1940 1200,2030 L1200,2165 L0,2165 Z" fill="var(--teal)"/>
  </svg>

  <header class="brand">
    <span class="brand-mark"></span>
    <span class="brand-name">Marlowe</span>
    <span class="brand-sub">Pain Relief Center</span>
  </header>

  <div class="slogan">
    <span class="slogan-title">Live Better</span>
    <span class="slogan-sub">Marlowe Pain Relief Center</span>
  </div>

  <div class="contact">
    For More<br>
    Information<br>
    Call Us :<br>
    (702) 555-0187
  </div>
  <div class="contact-rule"></div>

  <div class="language">Hablamos Español</div>

  <footer class="web-bar">marlowepaincarecenter.example</footer>
</main>
</body>
</html>
```